Business Card Design

slogan to use : 'Enhancing your natural beauty through all major brands of skincare, makeup and fragrances...'

I have just changed my business name from glow-harbourline to lumavista so would like a new business card. previous card is attached but happy for a new design

Lumavista logo to be used.

variety of brand logos to be advertised. brands include

varoni, mostrade, quenbury, tessa brandon, Pelisande, pure crystals, falque, zendra, omblue, del marco, clawsmith, velvet dawn, twig and thistle, rosa penhallow, complete wellness schedule, korvel.

please include a discount code : - 5% off next order - please enter 'qtix47' at checked to qualify'

facebook: glowharbourlineshop
twitter: glowharbour

Industry/Entity Type

Nutrition

Contact Information for Business Card

Dr Marina Voss
www.lumavista.co.uk
info@lumavista.co.uk

```html
<!DOCTYPE html>
<html lang="en">
<head>
<meta charset="utf-8">
<title>Lumavista Business Card</title>
<link rel="stylesheet" href="https://fonts.googleapis.com/css2?family=Open+Sans:ital,wght@0,400;0,600;1,400&display=swap">
<style>
  :root {
    --page: #ffffff;
    --berry: #a61d5c;
    --ink-light: #ffffff;
  }
  html, body {
    margin: 0;
    padding: 0;
    width: 1200px;
    height: 741px;
    overflow: hidden;
    background: var(--page);
  }
  .canvas {
    position: relative;
    width: 1200px;
    height: 741px;
    overflow: hidden;
    background: var(--page);
    font-family: "Open Sans", Arial, sans-serif;
  }
  .card {
    position: absolute;
    left: 48px;
    top: 44px;
    width: 1105px;
    height: 653px;
    background: var(--berry);
    overflow: hidden;
    color: var(--ink-light);
  }
  .floral-backdrop {
    position: absolute;
    left: 114px;
    top: 160px;
    width: 703px;
    height: 493px;
    background: radial-gradient(ellipse at 55% 45%, rgba(255,255,255,0.16) 0%, rgba(255,255,255,0.07) 45%, rgba(255,255,255,0) 75%);
  }
  .brand-name {
    position: absolute;
    left: 0;
    width: 100%;
    top: 80px;
    margin: 0;
    padding-left: 30px;
    box-sizing: border-box;
    text-align: center;
    font-size: 58px;
    font-weight: 400;
    line-height: 1;
  }
  .slogan {
    position: absolute;
    left: 123px;
    top: 180px;
    width: 960px;
    margin: 0;
    font-style: italic;
    font-size: 23px;
    line-height: 33px;
  }
  .offer {
    position: absolute;
    left: 34px;
    top: 287px;
    margin: 0;
    font-size: 25px;
    line-height: 35px;
  }
  .social {
    position: absolute;
    left: 34px;
    top: 373px;
    margin: 0;
    font-size: 25px;
    line-height: 36px;
  }
  .contact-panel {
    position: absolute;
    left: 613px;
    top: 275px;
    width: 492px;
    height: 164px;
    background: var(--page);
    color: var(--berry);
    text-align: center;
  }
  .contact-name {
    margin: 22px 0 14px;
    font-size: 34px;
    font-weight: 400;
    letter-spacing: 1px;
    line-height: 1;
  }
  .contact-line {
    margin: 0;
    font-size: 25px;
    line-height: 30px;
  }
  .stockists {
    position: absolute;
    inset: 0;
  }
  .stockist {
    position: absolute;
    transform: translate(-50%, -50%);
    white-space: nowrap;
    font-size: 22px;
    font-weight: 600;
    letter-spacing: 1px;
    line-height: 1;
  }
</style>
</head>
<body>
<div class="canvas">
  <div class="card">
    <div class="floral-backdrop" role="img" aria-label="Faint magnolia branch with blossoms and leaves behind the text"></div>

    <h1 class="brand-name">Lumavista</h1>

    <p class="slogan">Enhancing your natural Beauty through all major brands of skincare, makeup<br>and fragrances.....</p>

    <p class="offer">5% off next order - please enter 'qtix47'<br>at checked to qualify'</p>

    <p class="social">facebook: glowharbourlineshop<br>twitter: glowharbour</p>

    <div class="contact-panel">
      <h2 class="contact-name">DR MARINA VOSS</h2>
      <p class="contact-line">www.lumavista.co.uk</p>
      <p class="contact-line">info@lumavista.co.uk</p>
    </div>

    <div class="stockists">
      <span class="stockist" style="left:228px; top:528px;">DEL MARCO</span>
      <span class="stockist" style="left:447px; top:528px;">VELVET DAWN</span>
      <span class="stockist" style="left:676px; top:528px;">PELISANDE</span>
      <span class="stockist" style="left:910px; top:528px;">FALQUE</span>
      <span class="stockist" style="left:120px; top:591px;">MOSTRADE</span>
      <span class="stockist" style="left:330px; top:591px;">clawsmith</span>
      <span class="stockist" style="left:540px; top:591px;">Varoni</span>
      <span class="stockist" style="left:739px; top:591px;">ZENDRA</span>
      <span class="stockist" style="left:957px; top:591px;">korvel</span>
    </div>
  </div>
</div>
</body>
</html>
```